ONE PAGE WEB DESIGN NEEDED for Finance Company

We need a web design (ONE PAGE DESIGN ONLY) for a new finance website called Corvella Lending. Corvella Lending helps customers get the right loan, whether its a home loan, investment loan, business loan etc.

You are required to come up with just the homepage design. Professionalism and quality is the key factors in the successful design.

Here are a few design questions to help you out:

-
What information should be used on the page?
Ive provided a document which outlines all the information needed to put on homepage (attached to the brief - called corvella_page_info). Also see the Must Have section below on this brief.

-
What links should appear in the navigation/footer?:
The navigation should provide links to the following pages (NOTE: services link has subcategories):
1 Homepage
2 Services
- Home loans
- Investment loans
- Refinancing loans
- Business loans
3 About Us
4 FAQ
5 Contact Us

-
What colors should be used in the design?
Our company colors - Cyan: #2EADE3, Blue: #004B70, White. Feel free to submit designs with slight variations if you feel it improves the design.

-
What should the layout of the page be?
This is up to you to come up with - we are open to different layouts for the page design (as long as they capture the information effectively and making it easy to understand).

Target Market(s)

Potential Home owners, Families and Business Owners

Industry/Entity Type

Business

Requirements
Must have
• - Must contain our logo (attached as PNG and Illustrator file)
- Winning designer must supply a Photoshop file (PSD) that will allow us.
Nice to have
• - Should include photos/images of families, professional groups, tradespeople etc (you can use stock photos from PixelVaultImages and I will purchase them once you are selected as the winning design)
- Link to a loan calculator somewhere on front page with a button 'Find out how much you could borrow' (or maybe even try adding a loan calculator to the homepage if you think this would look good)
- Page should have a main headline "Finding the right loan for you" or "Corvella Lending finds the right loan for our customers."
- Must include Accreditation logos somewhere on the homepage (will try and supply these soon)
Should not have
• - Poor quality designs will not be considered
- Do not use clipart

```html
<!DOCTYPE html>
<html lang="en">
<head>
<meta charset="utf-8">
<title>Corvella Lending</title>
<link href="https://fonts.googleapis.com/css2?family=Oswald:wght@400;500&family=Ubuntu:wght@400;500;700&family=Open+Sans:wght@400;600&display=swap" rel="stylesheet">
<style>
:root{
  --cyan:#2eade3;
  --blue:#004b70;
  --navy:#0a5a8a;
  --nav-top:#1277b3;
  --nav-bottom:#0b5d91;
  --ink:#333;
  --grey:#888;
  --light:#eeeeee;
  --panel:#f4f4f4;
  --footer:#dcdcdc;
  --red:#e0231b;
}
*{margin:0;padding:0;box-sizing:border-box}
html,body{width:806px;height:1200px;overflow:hidden}
body{position:relative;background:#fff;font-family:"Open Sans",Arial,sans-serif;color:var(--ink)}
.abs{position:absolute}
a{color:inherit}

/* header */
.site-header{left:0;top:0;width:806px;height:81px;background:#fff}
.brand{left:104px;top:34px;display:flex;align-items:center;gap:7px;font-family:"Ubuntu",sans-serif;font-weight:500;font-size:17px;color:var(--cyan)}
.brand-dot{width:12px;height:12px;border-radius:50%;background:var(--blue)}
.support{left:568px;top:34px;display:flex;gap:8px;align-items:center}
.support-label{font-family:"Ubuntu",sans-serif;font-size:9px;color:#444}
.support-phone{font-family:"Ubuntu",sans-serif;font-size:16px;color:#222;letter-spacing:.5px}

/* navigation */
.main-nav{left:0;top:81px;width:806px;height:30px;background:linear-gradient(var(--nav-top),var(--nav-bottom))}
.nav-list{left:78px;top:0;display:flex;list-style:none;height:30px}
.nav-list li{font-family:"Ubuntu",sans-serif;font-weight:700;font-size:8px;color:#fff;padding:0 11px;line-height:30px;border-right:1px solid rgba(0,0,0,.25)}
.nav-list li:last-child{border-right:1px solid rgba(0,0,0,.25)}
.follow{left:568px;top:0;line-height:30px;font-family:"Ubuntu",sans-serif;font-weight:700;font-size:9px;color:#fff}
.social{top:8px;width:14px;height:14px;border-radius:50%;background:#fff;opacity:.9}

/* hero */
.hero{left:0;top:111px;width:806px;height:265px;background:linear-gradient(90deg,#d9cdbf 0%,#c9b49e 40%,#b49273 70%,#a78566 100%)}
.hero-panel{left:0;top:62px;width:382px;height:148px;background:rgba(255,255,255,.72)}
.hero-title{left:94px;top:76px;font-family:"Ubuntu",sans-serif;font-size:29px;color:var(--blue);letter-spacing:-.3px}
.hero-sub{left:94px;top:115px;font-family:"Ubuntu",sans-serif;font-size:15px;line-height:17px;color:#222;letter-spacing:-.4px;width:260px}
.hero-copy{left:94px;top:162px;font-family:"Ubuntu",sans-serif;font-size:8px;line-height:11px;color:#222;width:260px}

/* calculator */
.calculator{left:0;top:376px;width:806px;height:77px;background:#f0f0f3}
.calc-title{left:94px;top:22px;font-family:"Ubuntu",sans-serif;font-size:14px;color:#444}
.calc-sub{left:94px;top:39px;font-family:"Ubuntu",sans-serif;font-size:9px;color:#999}
.calc-q{left:238px;font-family:"Ubuntu",sans-serif;font-size:12px;color:var(--navy)}
.track{left:426px;width:168px;height:4px;border-radius:2px;background:#e1e1e4}
.track-fill{left:0;top:0;height:4px;border-radius:2px;background:var(--navy)}
.knob{top:-3px;width:10px;height:10px;border-radius:50%;background:#ddd;border:2px solid #888}
.pm{font-size:11px;color:#999}
.calc-box{left:636px;width:22px;height:13px;background:#fff;border:1px solid #ddd;font-size:8px;color:#888;text-align:center;line-height:11px}
.calc-unit{left:666px;font-size:9px;color:#888}
.calc-summary{left:238px;top:58px;font-family:"Ubuntu",sans-serif;font-size:12px;color:#999;letter-spacing:-.3px}
.calc-summary b{font-weight:400;color:#333}
.calc-summary em{font-style:normal;color:var(--cyan)}
.apply-btn{left:629px;top:53px;width:64px;height:19px;background:var(--cyan);border-radius:2px;color:#fff;font-family:"Ubuntu",sans-serif;font-size:9px;text-align:center;line-height:19px}

/* services */
.service{top:466px;height:142px;background:linear-gradient(#fff,#f1f1f1);border:1px solid #e3e3e3}
.service-head{left:0;top:0;right:0;height:34px;background:linear-gradient(#0d6aa2,var(--blue));color:#fff;font-family:"Ubuntu",sans-serif;font-size:14px;line-height:34px;padding-left:28px}
.service-head svg{position:absolute;left:12px;top:10px}
.service ul{position:absolute;left:6px;top:42px;list-style:none;width:130px}
.service li{font-size:9px;color:#333;text-decoration:underline;margin-bottom:5px;padding-left:10px;position:relative;line-height:12px}
.service li::before{content:"";position:absolute;left:0;top:4px;width:4px;height:4px;border-radius:50%;background:var(--navy)}

/* content */
.content{left:0;top:620px;width:806px;height:355px;background:var(--light)}
.photo-frame{background:#fafafa;border:1px solid #ddd;box-shadow:0 1px 3px rgba(0,0,0,.12)}
.photo{background:linear-gradient(135deg,#4a5560,#c9c2b6 50%,#6b6258)}
.pin{width:12px;height:12px;border-radius:50%;background:var(--red);box-shadow:1px 1px 2px rgba(0,0,0,.3)}
.section-title{font-family:"Oswald",sans-serif;font-size:16px;color:var(--blue);letter-spacing:-.2px}
.body-copy{font-family:Arial,sans-serif;font-size:8px;line-height:12px;color:#888}
.terms{left:95px;top:780px;width:617px;height:160px;background:#f6f6f6;border:1px solid #ddd;box-shadow:0 1px 3px rgba(0,0,0,.1)}
.terms-inner{left:6px;top:6px;width:603px;height:146px;background:#f3f3f3;border:1px solid #e6e6e6}
.terms-lead{font-family:"Oswald",sans-serif;font-size:9px;line-height:11px;color:#444;width:260px}
.more{font-size:8px;color:#333}

/* footer */
.site-footer{left:0;top:975px;width:806px;height:225px;background:var(--footer);border-top:2px solid #c8c8c8}
.foot-title{top:30px;font-family:"Oswald",sans-serif;font-size:18px;color:#444}
.foot-list{top:63px;list-style:none}
.foot-list li{font-size:8px;color:#777;line-height:16px;padding-left:14px;position:relative}
.foot-list li::before{content:"";position:absolute;left:2px;top:5px;width:6px;height:6px;border-radius:50%;background:var(--red)}
.field{left:422px;width:148px;background:#a9a9a9;border:1px solid #999;font-size:8px;color:#eee;padding:5px 10px}
.send-btn{left:515px;top:184px;width:54px;height:19px;background:#f4f4f4;border:1px solid #ccc;box-shadow:0 1px 2px rgba(0,0,0,.2);font-family:"Oswald",sans-serif;font-size:11px;color:var(--navy);text-align:center;line-height:18px}
.map{left:584px;top:68px;width:148px;height:107px;background:linear-gradient(135deg,#ece9e1,#dcd8cc 60%,#e8e3d2);border:1px solid #ccc}
.address{left:584px;top:185px;font-size:8px;line-height:10px;color:#444}
</style>
</head>
<body>

<header class="site-header abs">
  <div class="brand abs"><span class="brand-dot"></span>Corvella Lending</div>
  <div class="support abs">
    <svg width="28" height="28" viewBox="0 0 28 28" aria-hidden="true"><path d="M5 16a9 9 0 0 1 18 0" fill="none" stroke="#333" stroke-width="2.2"/><rect x="3" y="15" width="5" height="8" rx="2" fill="#333"/><rect x="20" y="15" width="5" height="8" rx="2" fill="#333"/><path d="M22 22q0 4-7 4" fill="none" stroke="#333" stroke-width="1.5"/></svg>
    <div><div class="support-label">24/7 Online Support Service</div><div class="support-phone">1-800-555-0142</div></div>
  </div>
</header>

<nav class="main-nav abs">
  <ul class="nav-list abs">
    <li>HOME</li><li>SERVICES &#9662;</li><li>ABOUT US</li><li>FAQ</li><li>CONTACT US</li>
  </ul>
  <div class="follow abs">Follow Us</div>
  <span class="social abs" style="left:630px" aria-label="Social link"></span>
  <span class="social abs" style="left:652px" aria-label="Social link"></span>
  <span class="social abs" style="left:674px" aria-label="Social link"></span>
  <span class="social abs" style="left:696px" aria-label="Social link"></span>
</nav>

<section class="hero abs" role="img" aria-label="Photo of a smiling young couple sitting among moving boxes in their new home">
  <div class="hero-panel abs"></div>
  <h1 class="hero-title abs" style="font-weight:400">CORVELLA LENDING</h1>
  <p class="hero-sub abs">FINDS THE RIGHT LOAN FOR OUR CUSTOMERS."</p>
  <p class="hero-copy abs">LOREM IPSUM DOLOR SIT AMET, CONSECTETUER ADIPISCING ELIT, SED DIAM NONUMMY NIBH EUISMOD TINCIDUNT UT LAOREET.</p>
</section>

<section class="calculator abs">
  <div class="calc-title abs">LOAN CALCULATOR</div>
  <div class="calc-sub abs">Calculate yourself</div>
  <div class="calc-q abs" style="top:14px">How much cash do you want?</div>
  <div class="calc-q abs" style="top:30px">How long do you want it for ?</div>
  <span class="pm abs" style="left:415px;top:14px">–</span>
  <span class="pm abs" style="left:415px;top:30px">–</span>
  <div class="track abs" style="top:21px"><div class="track-fill abs" style="width:57px"></div><div class="knob abs" style="left:52px"></div></div>
  <div class="track abs" style="top:37px"><div class="track-fill abs" style="width:30px"></div><div class="knob abs" style="left:26px"></div></div>
  <span class="pm abs" style="left:609px;top:14px">+</span>
  <span class="pm abs" style="left:609px;top:30px">+</span>
  <div class="calc-box abs" style="top:17px">291</div>
  <div class="calc-box abs" style="top:33px">21</div>
  <div class="calc-unit abs" style="top:17px">Dollars</div>
  <div class="calc-unit abs" style="top:33px">Days</div>
  <div class="calc-summary abs">You are borrowing <b>$ 291</b> + Interest &amp; Fees <b>$ 75.68</b> = Total to repay <em>$ 450</em></div>
  <div class="apply-btn abs">Apply Now</div>
</section>

<article class="service abs" style="left:94px;width:148px">
  <h2 class="service-head abs" style="font-weight:400"><svg width="10" height="13" viewBox="0 0 10 13" aria-hidden="true"><path d="M2 1l6 6-3 1 2 4-2 1-2-4-2 2z" fill="#fff"/></svg>Home loan</h2>
  <ul><li>Home buyers</li><li>First home buyers</li><li>Over 20 lenders</li></ul>
</article>
<article class="service abs" style="left:253px;width:149px">
  <h2 class="service-head abs" style="font-weight:400"><svg width="10" height="13" viewBox="0 0 10 13" aria-hidden="true"><path d="M2 1l6 6-3 1 2 4-2 1-2-4-2 2z" fill="#fff"/></svg>Investment loan</h2>
  <ul><li>Property investment</li><li>Interest only loans</li></ul>
</article>
<article class="service abs" style="left:412px;width:150px">
  <h2 class="service-head abs" style="font-weight:400"><svg width="10" height="13" viewBox="0 0 10 13" aria-hidden="true"><path d="M2 1l6 6-3 1 2 4-2 1-2-4-2 2z" fill="#fff"/></svg>Refinancing</h2>
  <ul><li>Refinancing for the best rate</li><li>Upsizing or downsizing</li><li>Change from a variable to a fixed rate</li></ul>
</article>
<article class="service abs" style="left:574px;width:150px">
  <h2 class="service-head abs" style="font-weight:400"><svg width="10" height="13" viewBox="0 0 10 13" aria-hidden="true"><path d="M2 1l6 6-3 1 2 4-2 1-2-4-2 2z" fill="#fff"/></svg>Bussiness Loan</h2>
  <ul><li>Long term</li><li>Short term</li><li>Equipment and Leasing</li></ul>
</article>

<section class="content abs">
  <div class="photo-frame abs" style="left:94px;top:17px;width:189px;height:105px">
    <div class="photo abs" role="img" aria-label="Photo of a couple meeting a financial advisor at a desk" style="left:7px;top:7px;width:174px;height:91px"></div>
  </div>
  <span class="pin abs" style="left:278px;top:56px"></span>
  <h2 class="section-title abs" style="left:310px;top:20px;font-weight:400">WELCOME TO CORVELLA LENDING</h2>
  <p class="body-copy abs" style="left:310px;top:51px;width:406px">Lorem ipsum dolor sit amet, consectetuer adipiscing elit, sed diam nonummy nibh euismod tincidunt ut laoreet dolore magna aliquam erat volutpat. Ut wisi enim ad minim veniam, quis nostrud exerci tation ullamcorper suscipit lobortis nisl ut aliquip ex ea commodo consequat. Duis autem vel eum iriure dolor in hendrerit in vulputate velit esse molestie consequat, vel illum dolore eu feugiat nulla facilisis at vero eros et accumsan et iusto odio dignissim qui blandit praesent luptatum.</p>
</section>

<section class="terms abs">
  <div class="terms-inner abs">
    <h2 class="section-title abs" style="left:22px;top:15px;font-weight:400">LOAN TERMS &amp; CONDITION</h2>
    <p class="terms-lead abs" style="left:22px;top:44px">Le Lorem Ipsum est le faux texte standard de l'imprimerie depuis les années 1500</p>
    <p class="body-copy abs" style="left:22px;top:73px;width:370px">Lorem ipsum dolor sit amet, consectetuer adipiscing elit, sed diam nonummy nibh euismod tincidunt ut laoreet dolore magna aliquam erat volutpat. Ut wisi enim ad minim veniam, quis nostrud exerci tation ullamcorper suscipit lobortis nisl ut aliquip ex ea commodo consequat. Duis autem vel eum iriure dolor.</p>
    <p class="more abs" style="left:22px;top:128px">more info &gt;&gt;</p>
    <div class="photo abs" role="img" aria-label="Close-up photo of a hand signing a loan document with a pen" style="left:402px;top:18px;width:168px;height:110px;background:linear-gradient(135deg,#2d3a48,#d8dde2 55%,#f2f2f2);border:3px solid #fff"></div>
  </div>
  <span class="pin abs" style="left:611px;top:73px"></span>
</section>

<footer class="site-footer abs">
  <h3 class="foot-title abs" style="left:98px;font-weight:400">LATEST POSTS</h3>
  <ul class="foot-list abs" style="left:98px">
    <li>Lorem ipsum dolor sit amet</li><li>Nam non diam eros</li><li>Vestibulum aliquet eros ut ipsum</li><li>Nullam blandit tristique lacus, quis</li><li>Ut quis ante dui, eget scelerisque</li><li>Praesent tincidunt dui id sapien</li><li>Vestibulum vel nisi vel ante ultrices</li>
  </ul>
  <h3 class="foot-title abs" style="left:262px;font-weight:400">SITE LINKS</h3>
  <ul class="foot-list abs" style="left:260px">
    <li>Home (we start here)</li><li>About (get to know us better)</li><li>Services (all we do)</li><li>Galleries (see our work)</li><li>Blog (the news)</li><li>Contact (get in touch with us)</li><li>Vestibulum (vel nisi vel ante)</li>
  </ul>
  <h3 class="foot-title abs" style="left:421px;font-weight:400">QUICK CONTACT</h3>
  <div class="field abs" style="top:68px;height:18px;padding-top:4px">Name</div>
  <div class="field abs" style="top:96px;height:18px;padding-top:4px">Email</div>
  <div class="field abs" style="top:123px;height:50px">Message</div>
  <div class="send-btn abs">SEND</div>
  <h3 class="foot-title abs" style="left:584px;font-weight:400">WE ON MAPS</h3>
  <div class="map abs" role="img" aria-label="Street map showing the office location"></div>
  <p class="address abs">18 Alder Row - Office Location<br>Westbrook - WB - 410220 - 0054 55501290</p>
</footer>

</body>
</html>
```